Icons for a business process application platform

Need a set of icons and visual process blocks for process designer UI

Industry/Entity Type

Business

```html
<!DOCTYPE html>
<html lang="en">
<head>
<meta charset="utf-8">
<title>Expense Process Flow</title>
<link rel="stylesheet" href="https://fonts.googleapis.com/css2?family=Open+Sans:wght@400;600&display=swap">
<style>
  :root {
    --canvas-bg: #ffffff;
    --block-fill: #f7f7f7;
    --block-border: #d6d8dc;
    --brand-purple: #3e2a5e;
    --connector-blue: #5e9ad6;
    --title-text: #6a6a6a;
    --subtitle-text: #a5a5a5;
    --diamond-fill: #f6f6f7;
    --diamond-border: #c9d3de;
    --white: #ffffff;
  }
  html, body {
    margin: 0;
    padding: 0;
    width: 1200px;
    height: 398px;
    overflow: hidden;
    background: var(--canvas-bg);
  }
  .process-canvas {
    display: block;
    width: 1200px;
    height: 398px;
    font-family: "Open Sans", Arial, sans-serif;
  }
  .connector { stroke: var(--connector-blue); stroke-width: 3; fill: none; }
  .arrowhead { fill: var(--connector-blue); }
  .block-frame { fill: var(--block-fill); stroke: var(--block-border); stroke-width: 3; }
  .icon-badge { fill: var(--brand-purple); }
  .icon-ring { fill: none; stroke: var(--white); stroke-width: 2.5; }
  .icon-glyph { fill: var(--white); }
  .icon-glyph-line { stroke: var(--brand-purple); stroke-width: 1.6; }
  .block-title { fill: var(--title-text); font-size: 17px; font-weight: 400; }
  .block-role { fill: var(--subtitle-text); font-size: 15px; font-weight: 400; }
  .gateway-shape { fill: var(--diamond-fill); stroke: var(--diamond-border); stroke-width: 3; }
  .gateway-table { fill: var(--brand-purple); }
  .gateway-cell { fill: var(--white); }
  .gateway-label { fill: var(--title-text); font-size: 8.5px; text-anchor: middle; }
</style>
</head>
<body>
<svg class="process-canvas" viewBox="0 0 1200 398" xmlns="http://www.w3.org/2000/svg" aria-label="Expense approval process flow">
  <defs>
    <marker id="arrow-tip" viewBox="0 0 10 10" refX="8" refY="5" markerWidth="4" markerHeight="4" orient="auto-start-reverse">
      <path class="arrowhead" d="M0,0 L10,5 L0,10 z"/>
    </marker>
  </defs>

  <!-- connectors -->
  <line class="connector" x1="346" y1="198" x2="534" y2="198" marker-end="url(#arrow-tip)"/>
  <line class="connector" x1="678" y1="198" x2="860" y2="198" marker-end="url(#arrow-tip)"/>
  <line class="connector" x1="606" y1="102" x2="606" y2="24" marker-end="url(#arrow-tip)"/>
  <line class="connector" x1="606" y1="294" x2="606" y2="372" marker-end="url(#arrow-tip)"/>

  <!-- initiator block -->
  <g class="process-block initiator-block">
    <rect class="block-frame" x="55" y="152" width="290" height="92"/>
    <circle class="icon-badge" cx="95" cy="198" r="27"/>
    <circle class="icon-ring" cx="95" cy="198" r="21"/>
    <g class="form-icon">
      <path class="icon-glyph" d="M84,183 H106 V207 L99,214 H84 Z"/>
      <path class="icon-badge" d="M99,214 V207 H106 Z"/>
      <line class="icon-glyph-line" x1="88" y1="189" x2="102" y2="189"/>
      <line class="icon-glyph-line" x1="88" y1="194" x2="102" y2="194"/>
      <line class="icon-glyph-line" x1="88" y1="199" x2="102" y2="199"/>
      <line class="icon-glyph-line" x1="88" y1="204" x2="97" y2="204"/>
    </g>
    <text class="block-title" x="146" y="189">Application Form</text>
    <text class="block-role" x="146" y="210">Initiator</text>
  </g>

  <!-- decision gateway -->
  <g class="decision-gateway">
    <polygon class="gateway-shape" points="606,102 678,198 606,294 534,198"/>
    <g class="table-icon">
      <rect class="gateway-table" x="579" y="149" width="55" height="52"/>
      <g class="gateway-cell">
        <rect x="582" y="161" width="11" height="8"/><rect x="595" y="161" width="11" height="8"/><rect x="608" y="161" width="11" height="8"/><rect x="621" y="161" width="10" height="8"/>
        <rect x="582" y="171" width="11" height="8"/><rect x="595" y="171" width="11" height="8"/><rect x="608" y="171" width="11" height="8"/><rect x="621" y="171" width="10" height="8"/>
        <rect x="582" y="181" width="11" height="8"/><rect x="595" y="181" width="11" height="8"/><rect x="608" y="181" width="11" height="8"/><rect x="621" y="181" width="10" height="8"/>
        <rect x="582" y="191" width="11" height="7"/><rect x="595" y="191" width="11" height="7"/><rect x="608" y="191" width="11" height="7"/><rect x="621" y="191" width="10" height="7"/>
      </g>
    </g>
    <text class="gateway-label" x="606" y="213">Route based on</text>
    <text class="gateway-label" x="606" y="225">expense amount</text>
  </g>

  <!-- approval block -->
  <g class="process-block approval-block">
    <rect class="block-frame" x="866" y="152" width="290" height="92"/>
    <circle class="icon-badge" cx="911" cy="198" r="27"/>
    <circle class="icon-ring" cx="911" cy="198" r="21"/>
    <g class="user-icon">
      <ellipse class="icon-glyph" cx="911" cy="191" rx="8" ry="10"/>
      <path class="icon-glyph" d="M895,213 C896,204 903,201 911,201 C919,201 926,204 927,213 Z"/>
    </g>
    <text class="block-title" x="962" y="189">Get Manager Approval</text>
    <text class="block-role" x="962" y="210">Approval</text>
  </g>
</svg>
</body>
</html>
```